Dorsey K. Wendell Business Card

We need a business card for our company Dorsey K. Wendell Heating & Plumbing to be distributed to potential customers. It should follow the color scheme of our logo and have a modern upscale and masculine look.

The logo is attached and the info below should also be included:

5187 W. Cedar Brook Rd.
Hollisburg, PA 17563

Russell T. Wendell
(717) 592-0817
russelltwendell@fernmail.net
dorseykwendell.net
PA #093148

Industry/Entity Type

Business

Contact Information for Business Card

5187 W. Cedar Brook Rd.
Hollisburg, PA 17563

Russell T. Wendell
(717) 592-0817
russelltwendell@fernmail.net
dorseykwendell.net
PA #093148

Colors

Designer to choose colors to be used in the design.

Requirements
Must have
• Information above included

```html
<!DOCTYPE html>
<html lang="en">
<head>
<meta charset="utf-8">
<title>Dorsey K. Wendell Business Card</title>
<link href="https://fonts.googleapis.com/css2?family=Open+Sans:wght@400;700&family=PT+Sans+Narrow:wght@700&display=swap" rel="stylesheet">
<style>
  :root {
    --stage: #2a2a2a;
    --card-white: #ffffff;
    --brand-blue: #0a55a0;
    --brand-green: #aecf3a;
    --text-gray: #555555;
    --divider: #9a9a9a;
  }
  * { margin: 0; padding: 0; box-sizing: border-box; }
  html, body {
    width: 1200px; height: 960px; overflow: hidden;
    background: var(--stage);
    font-family: "Open Sans", Arial, sans-serif;
  }
  .canvas { position: relative; width: 1200px; height: 960px; }

  .card { position: absolute; width: 600px; height: 343px; }
  .card--front { left: 314px; top: 113px; background: var(--card-white); }
  .card--back { left: 311px; top: 472px; background: var(--brand-green); }

  .brand { position: absolute; display: flex; align-items: center; gap: 10px; }
  .brand__square { width: 52px; height: 52px; flex: none; }
  .brand__name {
    font-family: "PT Sans Narrow", "Arial Narrow", sans-serif;
    font-weight: 700; text-transform: uppercase; line-height: 1.05;
  }
  .card--front .brand { left: 46px; top: 140px; }
  .card--front .brand__square { background: var(--brand-blue); }
  .card--front .brand__name { color: var(--brand-blue); font-size: 22px; }

  .card--back .brand { left: 142px; top: 130px; gap: 14px; }
  .card--back .brand__square { width: 72px; height: 72px; background: var(--card-white); }
  .card--back .brand__name { color: var(--card-white); font-size: 31px; }

  .divider {
    position: absolute; left: 312px; top: 97px; width: 2px; height: 150px;
    background: linear-gradient(to bottom, transparent, var(--divider) 50%, transparent);
  }

  .contact { position: absolute; left: 341px; top: 96px; color: var(--text-gray); }
  .contact__name {
    font-family: "PT Sans Narrow", "Arial Narrow", sans-serif;
    font-weight: 700; font-size: 25px; color: var(--brand-blue);
    text-transform: uppercase; margin-bottom: 8px; letter-spacing: 0.2px;
  }
  .contact__address { font-size: 14.5px; line-height: 20px; margin-bottom: 8px; }
  .contact__line { display: flex; align-items: center; gap: 7px; font-size: 14.5px; line-height: 19px; }
  .contact__line svg { width: 14px; height: 12px; fill: var(--brand-blue); flex: none; }

  .web-band { position: absolute; left: 0; top: 296px; width: 600px; }
  .web-band__rule { height: 3px; background: var(--brand-green); }
  .web-band__bar {
    height: 30px; margin: 1px 0; background: var(--brand-blue);
    color: var(--card-white); font-weight: 700; font-size: 15px;
    letter-spacing: 4.5px; text-align: center; line-height: 30px;
  }
</style>
</head>
<body>
<main class="canvas">
  <section class="card card--front" aria-label="Card front">
    <div class="brand">
      <span class="brand__square"></span>
      <span class="brand__name">Dorsey K. Wendell<br>Heating &amp; Plumbing</span>
    </div>
    <div class="divider"></div>
    <div class="contact">
      <h1 class="contact__name">Russell T. Wendell</h1>
      <p class="contact__address">5187 W. Cedar Brook Rd.<br>Hollisburg, PA 17563<br>PA #093148</p>
      <p class="contact__line">
        <svg viewBox="0 0 14 12" aria-hidden="true"><path d="M1 4C1 1 4 1 7 1s6 0 6 3l-3 1-1-2H5L4 5zM3 6l1-1h6l1 1 1 5H2z"/></svg>
        (717) 592-0817
      </p>
      <p class="contact__line">
        <svg viewBox="0 0 14 12" aria-hidden="true"><path d="M1 2h12L7 7zM1 3.5l6 5 6-5V10H1z"/></svg>
        russelltwendell@fernmail.net
      </p>
    </div>
    <div class="web-band">
      <div class="web-band__rule"></div>
      <div class="web-band__bar">www.dorseykwendell.net</div>
      <div class="web-band__rule"></div>
    </div>
  </section>

  <section class="card card--back" aria-label="Card back">
    <div class="brand">
      <span class="brand__square"></span>
      <span class="brand__name">Dorsey K. Wendell<br>Heating &amp; Plumbing</span>
    </div>
  </section>
</main>
</body>
</html>
```